Film Company needs Poster Design Project for upcoming film "CRANE"

At Marrowbend Films, we need a poster design for our upcoming feature film project "CRANE," America first 'rock and roll' star. Our film will cover Silas Wendell Crane's life his drinking, passion and writing. It will not be a horror film, but rather a biopic on his life.
Marrowbend Films is a full service film and television production company, founded by Dale Whitmore and Brevantis, LLC in 2006. Marrowbend Films’ mission is to blend artistic talent with engaging stories to create feature films and television that delight audiences of all ages.
We would like to see designs that embody Silas Wendell Crane as a person. The film will cover most of his famous poems/novels/short stories so any reference to "Hollow clock" or "The Orchard," etc...would work.
Thank you ALL for the amazing work you have submitted, you made it really hard for me to come up with one choice. I will make my decision by Wednesday.
Target audience 18 - 35
It Company

```html
<!DOCTYPE html>
<html lang="en">
<head>
<meta charset="utf-8">
<title>CRANE — Marrowbend Films</title>
<link href="https://fonts.googleapis.com/css2?family=Oswald:wght@500;600&display=swap" rel="stylesheet">
<style>
  :root {
    --sky-dark: #2b2d2e;
    --sky-mid: #6d7273;
    --sky-light: #b9bdbd;
    --hair-dark: #1c1c1c;
    --skin-light: #dcdcd8;
    --skin-shade: #9a9a96;
    --collar-light: #cfcfcb;
    --coat-dark: #161616;
    --title-red: #8c1a14;
    --title-edge: #5a0d09;
    --subtitle-white: #f4f4f2;
    --brand-orange: #e8862a;
    --sketch-grey: #8a8a88;
  }
  * { margin: 0; padding: 0; box-sizing: border-box; }
  html, body { width: 849px; height: 1200px; overflow: hidden; background: var(--sky-dark); }
  .poster {
    position: relative;
    width: 849px;
    height: 1200px;
    overflow: hidden;
    font-family: "Oswald", "Arial Narrow", sans-serif;
  }
  .stormy-sky {
    position: absolute; inset: 0;
    background:
      radial-gradient(ellipse 45% 25% at 12% 22%, rgba(205,208,208,.6), transparent 70%),
      radial-gradient(ellipse 40% 22% at 90% 28%, rgba(195,198,198,.5), transparent 70%),
      radial-gradient(ellipse 40% 22% at 8% 50%, rgba(185,190,190,.6), transparent 70%),
      linear-gradient(180deg, #3a3c3d 0%, var(--sky-mid) 30%, #5d6262 55%, #3a3c3c 75%, var(--sky-dark) 100%);
  }
  .author-portrait {
    position: absolute;
    left: 0; top: 0;
    width: 849px; height: 1200px;
  }
  .cat-sketch {
    position: absolute;
    left: 25px; top: 805px;
    width: 135px; height: 395px;
    background: radial-gradient(ellipse 55% 40% at 55% 30%, rgba(150,150,148,.7), rgba(40,40,40,.4) 60%, transparent 80%);
  }
  .raven-sketch {
    position: absolute;
    left: 645px; top: 815px;
    width: 155px; height: 385px;
    background: radial-gradient(ellipse 50% 50% at 50% 40%, rgba(225,225,222,.7), rgba(120,120,118,.35) 60%, transparent 80%);
  }
  .studio-name {
    position: absolute;
    left: 30px; top: 112px;
    width: 196px;
    text-align: center;
    font-weight: 500;
    font-size: 19px;
    line-height: 1;
    letter-spacing: 1px;
    color: var(--brand-orange);
    text-transform: uppercase;
  }
  .film-title {
    position: absolute;
    left: 0; right: 0; top: 685px;
    text-align: center;
    font-weight: 500;
    font-size: 300px;
    line-height: 1;
    letter-spacing: 0;
    color: var(--title-red);
    -webkit-text-stroke: 2px var(--title-edge);
    transform: scaleX(0.9);
  }
  .tagline {
    position: absolute;
    left: 0; right: 0; top: 1020px;
    text-align: center;
    font-weight: 500;
    font-size: 46px;
    line-height: 1;
    letter-spacing: 0.5px;
    color: var(--subtitle-white);
    text-shadow: 0 2px 4px rgba(0,0,0,.7);
  }
</style>
</head>
<body>
  <main class="poster">
    <div class="stormy-sky" role="img" aria-label="Dark stormy clouds over a grey sea"></div>

    <svg class="author-portrait" viewBox="0 0 849 1200" role="img" aria-label="Black-and-white period portrait of Silas Wendell Crane in a dark coat and cravat">
      <defs>
        <filter id="soften" x="-20%" y="-20%" width="140%" height="140%">
          <feGaussianBlur stdDeviation="10"/>
        </filter>
        <radialGradient id="skin-tone" cx="50%" cy="40%" r="60%">
          <stop offset="0%" stop-color="var(--skin-light)"/>
          <stop offset="70%" stop-color="#bcbcb8"/>
          <stop offset="100%" stop-color="var(--skin-shade)"/>
        </radialGradient>
        <linearGradient id="collar-tone" x1="0" y1="0" x2="0" y2="1">
          <stop offset="0%" stop-color="var(--collar-light)"/>
          <stop offset="100%" stop-color="#8e8e8a"/>
        </linearGradient>
      </defs>
      <g filter="url(#soften)">
        <path class="portrait-coat" d="M170 1200 L200 760 Q260 640 420 620 Q600 630 680 720 L800 1200 Z" fill="var(--coat-dark)"/>
        <ellipse class="portrait-hair" cx="470" cy="330" rx="210" ry="280" fill="var(--hair-dark)"/>
        <path class="portrait-collar" d="M300 590 Q450 560 600 600 L610 700 Q450 680 300 700 Z" fill="url(#collar-tone)"/>
        <ellipse class="portrait-head" cx="455" cy="400" rx="155" ry="205" fill="url(#skin-tone)"/>
      </g>
    </svg>

    <div class="cat-sketch" role="img" aria-label="Sketch of a snarling black cat"></div>
    <div class="raven-sketch" role="img" aria-label="Sketch of a raven perched on a bust"></div>

    <div class="studio-name">Marrowbend Films</div>

    <h1 class="film-title">CRANE</h1>
    <p class="tagline">AMERICA FIRST ’ROCK AND ROLL’ STAR</p>
  </main>
</body>
</html>
```